Business Card Design Project

New Business Card design for Varodine Technology Ltd using new Logo and new Tagline for staffing company.

About us from our website - www.varodine.example:

VaroDine is a leading and recognized Electronic Entertainment, Workforce Augmentation, and Project Management solutions provider with clients in Electronic Entertainment, Legal, Technology, Government and other verticals that range in size from start up organizations to Zenlar 500 companies. VaroDine is certified as an 8(a) minority and woman owned enterprise, established in 1998.

Target Market(s)

Companies in Electronic Entertainment, Legal, Government and Technology

Industry/Entity Type

Business

Requirements
Must have
• Must include in small letters the following information on back:

Established in 1998
8(a)(w)(e), Cage #7KRT9, DUNS #462137580

Front should have the following:
Derek Holloway
Vice President
5820 Birchmont Road
Fallowby, FB 482917
555-318-2746 X 100
555-902-6613 Fax
555-318-2746 Toll Free
name@varodine.example

Our Tagline: Connect • Collaborate • Achieve

```html
<!DOCTYPE html>
<html lang="en">
<head>
<meta charset="utf-8">
<title>VaroDine Business Card</title>
<link href="https://fonts.googleapis.com/css2?family=Barlow+Semi+Condensed:wght@400;600&display=swap" rel="stylesheet">
<style>
  :root {
    --page-bg: #ffffff;
    --card-white: #ffffff;
    --ink-navy: #123a73;
    --brand-grey: #58595b;
    --brand-blue: #1565c0;
    --steel-dark: #2a3038;
    --steel-mid: #6f7884;
    --steel-light: #aab3bd;
    --back-name: #8a8f96;
    --back-text: #f2f4f6;
  }
  html, body {
    margin: 0;
    padding: 0;
    width: 1200px;
    height: 720px;
    overflow: hidden;
    background: var(--page-bg);
    font-family: "Barlow Semi Condensed", sans-serif;
  }
  .canvas {
    position: relative;
    width: 1200px;
    height: 720px;
  }
  .card {
    position: absolute;
    top: 214px;
    width: 496px;
    height: 280px;
    box-shadow: 3px 4px 8px rgba(0, 0, 0, 0.35);
    overflow: hidden;
  }
  .card-front {
    left: 80px;
    background: var(--card-white);
  }
  .card-back {
    left: 630px;
    background: var(--steel-dark);
  }

  /* Front */
  .contact {
    position: absolute;
    left: 29px;
    top: 33px;
    color: var(--ink-navy);
    font-size: 16px;
    line-height: 19.5px;
    font-weight: 400;
  }
  .contact p { margin: 0; }
  .contact .group + .group { margin-top: 19.5px; }

  .brand-name {
    position: absolute;
    left: 0;
    width: 100%;
    text-align: center;
    margin: 0;
    font-weight: 600;
    line-height: 1;
  }
  .front-brand {
    left: 240px;
    width: 226px;
    top: 60px;
    font-size: 58px;
    color: var(--brand-grey);
  }
  .tagline {
    position: absolute;
    left: 240px;
    width: 226px;
    top: 162px;
    margin: 0;
    text-align: center;
    color: var(--ink-navy);
    font-size: 18px;
    white-space: nowrap;
  }

  /* Back */
  .back-texture {
    position: absolute;
    inset: 0;
    background:
      radial-gradient(ellipse at 50% 30%, var(--steel-light) 0%, var(--steel-mid) 45%, var(--steel-dark) 100%);
  }
  .back-brand {
    top: 105px;
    font-size: 72px;
    color: var(--back-name);
  }
  .back-facts {
    position: absolute;
    left: 32px;
    right: 20px;
    top: 251px;
    margin: 0;
    color: var(--back-text);
    font-size: 15px;
    white-space: nowrap;
  }
  .back-facts .established { display: inline-block; width: 147px; }
</style>
</head>
<body>
<main class="canvas">
  <section class="card card-front" aria-label="Business card front">
    <div class="contact">
      <div class="group">
        <p class="person-name">Derek Holloway</p>
        <p class="person-title">Vice President</p>
      </div>
      <div class="group">
        <p>5820 Birchmont Road</p>
        <p>Fallowby, FB 482917</p>
      </div>
      <div class="group">
        <p>555-318-2746 X 100</p>
        <p>555-902-6613 Fax</p>
        <p>555-318-2746 Toll Free</p>
      </div>
      <div class="group">
        <p>name@varodine.example</p>
      </div>
    </div>
    <p class="brand-name front-brand">VaroDine</p>
    <p class="tagline">Connect • Collaborate • Achieve</p>
  </section>

  <section class="card card-back" aria-label="Business card back">
    <div class="back-texture" role="img" aria-label="Brushed steel backdrop with curved horizontal grooves"></div>
    <p class="brand-name back-brand">VaroDine</p>
    <p class="back-facts"><span class="established">Established in 1998</span>8(a)(w)(e), Cage #7KRT9, DUNS #462137580</p>
  </section>
</main>
</body>
</html>
```